tinyTallies Resource Book - 10 maths tasks to do outside

I need a 22 (11 pages back to back) page A6 sized book produced to standard for submission to professional printer. Needs to be as .pdf file showing guide lines and allowances for colour bleed. I have text already written and submitted as attachment in a Word file with margins set to A6 size. The theme of the materials is "Nature Play" so using lots of pictures from nature (Australia preferably) and showing lots of patterns in nature (rocks, leaves, flower petals etc). Some of the tasks refer to specific activities, such as "shadows" and "floating" so would be great to illustrate appropriately. The big emphasis is on learning outside the classroom, getting kids to engage actively with nature. I would like to see the pages as full colour - so not white background. The book itself will be spiral bound along the top edge so a margin of at least 1cm will be required at the top of each page (or the bottom of even numbered pages). Book will be printed on plastic laminated matte paper for outdoor use. Font size needs to be big enough to read. Fonts sizes, alignments and page numbers are all different at the moment and need to be standardised. One photo is included in a page as a sample if you can use it, otherwise disregard. Logo for Wattleford Numeracy Guild is also included to have as part of the acknowledgements at the back of the book.

Target Market(s)

Book is for early childhood and preschool teachers.

Industry/Entity Type

Education

Font styles to use
Sans Serif

Requirements
Must have
• Colour and appeal.
Nice to have
• Use of natural colours instead of bright catchy colours but that is your call.
Should not have
• American spelling

```html
<!DOCTYPE html>
<html lang="en-AU">
<head>
<meta charset="utf-8">
<title>Same Same Different – Task Card</title>
<link rel="stylesheet" href="https://fonts.googleapis.com/css2?family=Jost:ital,wght@0,700;0,800;1,700&family=Didact+Gothic&display=swap">
<style>
  :root {
    --paper: #ffffff;
    --trim: #6b6b6b;
    --sea-deep: #3f6f9e;
    --sea-light: #a9c3d8;
    --foam: #e6ebe9;
    --sand-light: #dcc7a6;
    --sand: #cdb38c;
    --sand-dark: #bca07a;
    --heading-blue: #2b3c93;
    --body-ink: #2b2622;
    --bullet-red: #d6262d;
    --pebble-green: #7c9a6f;
    --pebble-rose: #9b5a5c;
  }
  * { margin: 0; padding: 0; box-sizing: border-box; }
  html, body { width: 892px; height: 1200px; overflow: hidden; background: var(--paper); }
  .sheet { position: relative; width: 892px; height: 1200px; }
  .crop-marks { position: absolute; inset: 0; }
  .page {
    position: absolute; left: 53px; top: 56px; width: 785px; height: 1090px; overflow: hidden;
    background: linear-gradient(180deg,
      var(--sea-deep) 0%, var(--sea-light) 8%, var(--foam) 15%, var(--sand-light) 21%,
      var(--sand) 55%, var(--sand-dark) 100%);
  }
  .page > * { position: absolute; }
  .task-title {
    left: 0; right: 0; top: 94px; text-align: center;
    font: 800 46px/1 "Jost", sans-serif; color: var(--heading-blue);
    text-shadow: -2px -2px 0 #fff, 2px -2px 0 #fff, -2px 2px 0 #fff, 2px 2px 0 #fff,
                 0 3px 0 #fff, 3px 0 0 #fff, 0 -3px 0 #fff, -3px 0 0 #fff;
  }
  .outcome {
    left: 40px; right: 40px; top: 160px; text-align: center;
    font: 700 31px/43px "Jost", sans-serif; color: var(--heading-blue);
    text-shadow: -1px -1px 0 #fff, 1px -1px 0 #fff, -1px 1px 0 #fff, 1px 1px 0 #fff;
  }
  .lead {
    left: 73px; font: italic 700 25px/36px "Jost", sans-serif; color: var(--heading-blue);
  }
  .lead-children { top: 256px; width: 660px; }
  .lead-educators { top: 466px; }
  .lead-task { top: 684px; }
  .body-text {
    left: 144px; width: 560px; font: 29px/45.5px "Didact Gothic", sans-serif; color: var(--body-ink);
  }
  .body-children { top: 330px; }
  .body-educators { top: 502px; }
  .opportunities { left: 132px; top: 718px; list-style: none;
    font: 29px/40px "Didact Gothic", sans-serif; color: var(--body-ink); }
  .opportunities li { position: relative; padding-left: 33px; }
  .opportunities li::before {
    content: ""; position: absolute; left: 5px; top: 11px; width: 17px; height: 17px;
    background: var(--bullet-red); transform: rotate(45deg);
  }
  .pebbles {
    left: 563px; top: 680px; width: 145px; height: 216px; border-radius: 60px;
    background: linear-gradient(160deg, var(--pebble-green) 0%, var(--pebble-green) 55%, var(--pebble-rose) 100%);
    opacity: .85;
  }
</style>
</head>
<body>
<div class="sheet">
  <svg class="crop-marks" width="892" height="1200" viewBox="0 0 892 1200" aria-hidden="true">
    <g stroke="var(--trim)" stroke-width="1">
      <line x1="74" y1="36" x2="74" y2="74"/><line x1="36" y1="54" x2="74" y2="54"/>
      <line x1="53" y1="0" x2="53" y2="40"/><line x1="0" y1="74" x2="40" y2="74"/>
      <line x1="818" y1="36" x2="818" y2="74"/><line x1="818" y1="54" x2="856" y2="54"/>
      <line x1="838" y1="0" x2="838" y2="40"/><line x1="852" y1="74" x2="892" y2="74"/>
      <line x1="74" y1="1126" x2="74" y2="1164"/><line x1="36" y1="1146" x2="74" y2="1146"/>
      <line x1="53" y1="1160" x2="53" y2="1200"/><line x1="0" y1="1126" x2="40" y2="1126"/>
      <line x1="818" y1="1126" x2="818" y2="1164"/><line x1="818" y1="1146" x2="856" y2="1146"/>
      <line x1="838" y1="1160" x2="838" y2="1200"/><line x1="852" y1="1126" x2="892" y2="1126"/>
    </g>
  </svg>

  <main class="page" role="img" aria-label="Beach photograph: gentle waves washing onto wet sand">
    <h1 class="task-title">3. Same Same Different</h1>
    <h2 class="outcome">EYLF – Outcome 2: Children are connected with and contribute to their world</h2>

    <p class="lead lead-children">Children respond to diversity with respect when they...</p>
    <p class="body-text body-children">notice and react in positive ways to similarities and differences among people</p>

    <p class="lead lead-educators">Educators promote this learning when they...</p>
    <p class="body-text body-educators">plan experiences and provide resources that broaden children’s perspectives and encourage appreciation of diversity</p>

    <p class="lead lead-task">This task provides an opportunity to:</p>
    <ul class="opportunities">
      <li>explore the concepts<br>of “same” and “different”</li>
      <li>discuss diversity</li>
      <li>model and sort based<br>on specific criteria</li>
      <li>celebrate similarities and differences</li>
    </ul>

    <div class="pebbles" role="img" aria-label="Four polished speckled pebbles, three green and one rose-red"></div>
  </main>
</div>
</body>
</html>
```